I work in creative/artistic projects across different mediums.
It needs to communicate creativity, style, sexy, uniqueness, individuality and sophistication.
It should not look corporate.
Colours I like are black silver gold deep purple, chocolate, orchid.
It doesn't have to make use of all these colours.
I do not like bright primary colors.
Updates

Project Deadline Extended
Reason: Still in the communication process and to allow the person enough time to finish the design. Though i should know in the next day or two. Thank you.

Target Market(s)

creatives and companies wanting to inject creativity into thier business.

Industry/Entity Type

Work

Contact Information for Business Card

Lionel Crowthwick
0418359026
lionel@lionelcrowthwick.com

quietsilverhour.com.au

Requirements
Should not have
• Anything corporate OR OLD FASHIONED

```html
<!DOCTYPE html>
<html lang="en">
<head>
<meta charset="utf-8">
<title>Lionel Crowthwick — Business Card</title>
<link rel="stylesheet" href="https://fonts.googleapis.com/css2?family=Libre+Bodoni:ital,wght@1,400&display=swap">
<style>
  :root {
    --page-bg: #ecebee;
    --card-base: #0f0f11;
    --card-plum: #1c1a21;
    --card-black: #0c0c0d;
    --card-chocolate: #1d1814;
    --gold: #e2b434;
    --silver: #e4e2e6;
    --card-w: 912px;
    --card-h: 563px;
  }
  * { margin: 0; padding: 0; box-sizing: border-box; }
  html, body {
    width: 1200px;
    height: 905px;
    overflow: hidden;
    background: var(--page-bg);
  }
  .business-card {
    position: absolute;
    left: 50%;
    top: 50%;
    width: var(--card-w);
    height: var(--card-h);
    transform: translate(-50%, -50%) scale(1.14);
    background: var(--card-base);
    overflow: hidden;
    box-shadow: 0 10px 30px rgba(0, 0, 0, 0.25);
    font-family: "Libre Bodoni", "Bodoni Moda", Georgia, serif;
    font-style: italic;
    font-weight: 400;
  }
  .card-facets {
    position: absolute;
    inset: 0;
    width: 100%;
    height: 100%;
  }
  .facet-plum { fill: var(--card-plum); }
  .facet-black { fill: var(--card-black); }
  .facet-chocolate { fill: var(--card-chocolate); }
  .identity {
    position: absolute;
    left: 0;
    right: 0;
    top: 218px;
    text-align: center;
    color: var(--gold);
  }
  .identity-name {
    font-size: 41px;
    line-height: 1;
    letter-spacing: 0.2px;
  }
  .identity-phone {
    margin-top: 12px;
    font-size: 29px;
    line-height: 1;
    letter-spacing: 1px;
  }
  .contact-line {
    position: absolute;
    left: 56px;
    right: 53px;
    top: 464px;
    display: flex;
    justify-content: space-between;
    color: var(--silver);
    font-size: 28px;
    line-height: 1;
  }
</style>
</head>
<body>
  <main class="business-card">
    <svg class="card-facets" viewBox="0 0 912 563" preserveAspectRatio="none" aria-hidden="true">
      <rect class="facet-black" x="0" y="0" width="912" height="563"/>
      <polygon class="facet-plum" points="0,0 600,0 40,563 0,563"/>
      <polygon class="facet-chocolate" points="494,106 912,530 912,563 350,563 350,251"/>
    </svg>

    <section class="identity">
      <h1 class="identity-name" style="font-weight:400">Lionel Crowthwick</h1>
      <p class="identity-phone">0418359026</p>
    </section>

    <footer class="contact-line">
      <span class="contact-email">lionel@lionelcrowthwick.com</span>
      <span class="contact-web">www.quietsilverhour.com.au</span>
    </footer>
  </main>
</body>
</html>
```